Banner Design Project

We are an Australian online lighting store based in Sydney.
Our website is "www.trelvamart.com.au"
We need someone you can create a 2 banners for our homepage.
We will have 3 banners rotating, the first banner will be our actual banner, the second one will be advertising Free Shipping Insurance and the third will advertising the 30 Day money back guaranty.
Don't be afraid to use words like Risk Free, 30 Day Money back Guaranty! etc....
The banner size:
599 x 186 px
The format should be given in .psd and .jpg
We need something slick and attractive that looks very promotional.
The banner should have the same look and feel as the website.
We are looking for someone long term, so if the job goes well, we might ask the person to design regularly for us in the future.

```html
<!DOCTYPE html>
<html lang="en">
<head>
<meta charset="utf-8">
<title>Trelvamart – Lighting Store</title>
<link rel="stylesheet" href="https://fonts.googleapis.com/css2?family=PT+Sans:wght@400;700&family=Roboto+Slab:wght@700;800&display=swap">
<style>
  :root {
    --orange: #f58220;
    --orange-light: #f9a04a;
    --navy: #1f5b8f;
    --nav-dark: #1a4f80;
    --text: #222;
    --muted: #555;
    --line: #c9c9c9;
    --panel: #ececec;
    --panel-dark: #e0e0e0;
    --banner-blue: #2a6aa8;
    --white: #fff;
  }
  * { box-sizing: border-box; margin: 0; padding: 0; }
  html, body { width: 1200px; height: 519px; overflow: hidden; }
  body {
    position: relative;
    background: linear-gradient(#f4f4f4, #ffffff 120px);
    font-family: "PT Sans", Arial, sans-serif;
    color: var(--text);
  }
  .abs { position: absolute; }

  /* header */
  .brand { left: 30px; top: 36px; display: flex; align-items: center; gap: 12px; }
  .brand-dot { width: 40px; height: 40px; border-radius: 50%; background: var(--orange); }
  .brand-name { font-size: 58px; font-weight: 700; color: var(--orange); line-height: 1; letter-spacing: -1px; }

  .search { left: 412px; top: 53px; width: 487px; height: 40px; display: flex; }
  .search-field {
    flex: 1; border: 3px solid #cfcfcf; border-right: none; background: var(--white);
    font-size: 17px; color: #888; padding: 0 14px; display: flex; align-items: center;
  }
  .search-btn {
    width: 99px; background: linear-gradient(var(--orange-light), var(--orange));
    color: var(--white); font-weight: 700; font-size: 18px;
    display: flex; align-items: center; justify-content: center;
  }

  .advice { left: 960px; top: 22px; width: 200px; text-align: center; color: var(--muted); }
  .advice-title { font-size: 19px; }
  .advice-phone { font-size: 29px; margin-top: 2px; letter-spacing: 0.5px; }
  .advice-hours { font-size: 18px; margin-top: 2px; }

  /* navigation */
  .main-nav {
    left: 17px; top: 122px; width: 1183px; height: 37px;
    background: linear-gradient(var(--navy), var(--nav-dark));
  }
  .main-nav span { position: absolute; top: 9px; color: var(--white); font-size: 15px; }

  /* sidebar */
  .sidebar { left: 17px; top: 159px; width: 229px; height: 360px; background: var(--white); }
  .side-heading { position: absolute; left: 24px; font-size: 17px; font-weight: 700; }
  .side-rule { position: absolute; left: 0; width: 229px; border-top: 1px solid var(--line); }
  .side-link { position: absolute; left: 23px; font-size: 13px; }

  /* hero */
  .hero {
    left: 247px; top: 159px; width: 722px; height: 225px;
    background: linear-gradient(90deg, #ffffff 30%, #eef0f3 100%);
    border: 1px solid #ddd; overflow: hidden;
  }
  .hero-photo {
    position: absolute; left: 6px; top: 0; width: 262px; height: 225px;
    background: linear-gradient(160deg, #e9ebee 0%, #b8bcc3 55%, #5a4a44 100%);
  }
  .hero-arc { position: absolute; left: 250px; top: -40px; }
  .hero-big {
    position: absolute; left: 290px; top: 18px;
    font-family: "Roboto Slab", Georgia, serif; font-weight: 800;
    font-size: 120px; line-height: 1; color: var(--banner-blue); letter-spacing: 1px;
  }
  .hero-sub {
    position: absolute; left: 292px; top: 150px;
    font-family: "Roboto Slab", Georgia, serif; font-weight: 700;
    font-size: 29px; color: var(--banner-blue);
  }

  /* newsletter */
  .newsletter { left: 253px; top: 408px; width: 704px; height: 69px; background: var(--panel); }
  .news-icon {
    position: absolute; left: 12px; top: -8px; width: 70px; height: 72px;
    background: linear-gradient(135deg, #f3f3f3, #c5c8cc); transform: rotate(-12deg);
    border: 1px solid #bbb;
  }
  .news-title { position: absolute; left: 101px; top: 6px; font-size: 17px; font-weight: 700; }
  .news-title b { color: var(--navy); }
  .news-label { position: absolute; left: 125px; top: 36px; font-size: 16px; }
  .news-input { position: absolute; left: 217px; top: 34px; width: 309px; height: 26px; background: var(--white); border: 1px solid #bbb; }
  .news-btn {
    position: absolute; left: 530px; top: 36px; width: 84px; height: 22px;
    background: linear-gradient(var(--orange-light), var(--orange)); color: var(--white);
    font-weight: 700; font-size: 15px; text-align: center; line-height: 22px;
  }
  .lower-strip { left: 253px; top: 507px; width: 716px; height: 12px; background: var(--panel-dark); }

  /* cart column */
  .cart-col { left: 972px; top: 159px; width: 228px; height: 360px; background: var(--white); }
  .cart-icon { position: absolute; left: 25px; top: 38px; }
  .cart-title { position: absolute; left: 87px; top: 34px; font-size: 22px; font-weight: 700; line-height: 1.25; }
  .cart-line { position: absolute; left: 23px; font-size: 17px; }
  .cart-line b { font-weight: 700; }
  .checkout {
    position: absolute; left: 23px; top: 177px; width: 181px; height: 38px;
    background: linear-gradient(var(--orange-light), var(--orange));
    color: var(--white); font-size: 18px; font-weight: 700; text-align: center; line-height: 38px;
  }
  .why-box {
    position: absolute; left: 0; top: 227px; width: 228px; height: 67px;
    background: var(--panel); text-align: center; line-height: 67px;
    color: var(--navy); font-size: 21px; font-weight: 700;
  }
  .why-tick { position: absolute; left: 24px; top: 318px; }
  .why-item { position: absolute; left: 49px; top: 322px; font-size: 15px; line-height: 1.15; }
</style>
</head>
<body>

<header>
  <div class="abs brand"><span class="brand-dot"></span><span class="brand-name">Trelvamart</span></div>

  <div class="abs search">
    <div class="search-field">Type in Keyword, Brand or item#</div>
    <div class="search-btn">SEARCH</div>
  </div>

  <div class="abs advice">
    <div class="advice-title">Need Expert Advice?</div>
    <div class="advice-phone">1300 555 214</div>
    <div class="advice-hours">Mon-Fri 9am - 5pm</div>
  </div>
</header>

<nav class="abs main-nav">
  <span style="left:29px">Home</span>
  <span style="left:142px">About Us</span>
  <span style="left:280px">Testimonials</span>
  <span style="left:433px">Customer Care</span>
  <span style="left:605px">Contact Us</span>
  <span style="left:899px">My Shortlist</span>
  <span style="left:1010px">My Account</span>
  <span style="left:1124px">Login</span>
</nav>

<aside class="abs sidebar">
  <div class="side-heading" style="top:10px">Indoor Lighting</div>
  <div class="side-rule" style="top:38px"></div>
  <div class="side-link" style="top:51px">Ceiling Fans</div>
  <div class="side-link" style="top:79px">Ceiling Lights</div>
  <div class="side-link" style="top:107px">Wall Lights</div>
  <div class="side-link" style="top:135px">Table and Floor Lamps</div>
  <div class="side-link" style="top:163px">Kids Lighting</div>
  <div class="side-link" style="top:190px">LED / Energy Savers</div>
  <div class="side-rule" style="top:218px"></div>
  <div class="side-heading" style="top:227px">Outdoor Lighting</div>
  <div class="side-rule" style="top:256px"></div>
  <div class="side-link" style="top:269px">Garden Lights</div>
  <div class="side-link" style="top:297px">LED/Energy Savers</div>
  <div class="side-link" style="top:324px">In Ground Lights</div>
  <div class="side-link" style="top:352px">Bollards/Post Lights</div>
</aside>

<section class="abs hero">
  <svg class="hero-arc" width="200" height="320" viewBox="0 0 200 320" aria-hidden="true">
    <path d="M180 0 A200 200 0 0 0 180 320" fill="none" stroke="#dfe3e8" stroke-width="10"/>
  </svg>
  <div class="hero-photo" role="img" aria-label="Photo of a smiling customer service representative"></div>
  <div class="hero-big">30 Day</div>
  <div class="hero-sub">Money back Guaranty!</div>
</section>

<section class="abs newsletter">
  <div class="news-icon" role="img" aria-label="Envelope illustration"></div>
  <div class="news-title"><b>Join the Trelvamart Newsletter</b> - Sales, special offers and more</div>
  <div class="news-label">Enter Email:</div>
  <div class="news-input"></div>
  <div class="news-btn">Sign Up</div>
</section>
<div class="abs lower-strip"></div>

<aside class="abs cart-col">
  <svg class="cart-icon" width="48" height="46" viewBox="0 0 48 46" aria-hidden="true">
    <rect x="1" y="1" width="46" height="44" rx="6" fill="#f2f2f2" stroke="#bbb"/>
    <path d="M10 14 h5 l4 14 h15 l3 -10 h-20" fill="none" stroke="#333" stroke-width="2.5" stroke-linejoin="round"/>
    <circle cx="21" cy="33" r="2.5" fill="#333"/>
    <circle cx="32" cy="33" r="2.5" fill="#333"/>
  </svg>
  <div class="cart-title">Shopping<br>Cart</div>
  <div class="cart-line" style="top:110px"><b>Items:</b> 0</div>
  <div class="cart-line" style="top:132px"><b>Total:</b> $0.00</div>
  <div class="checkout">CHECKOUT</div>
  <div class="why-box">Why Trelvamart?</div>
  <svg class="why-tick" width="20" height="20" viewBox="0 0 20 20" aria-hidden="true">
    <path d="M2 11 l5 6 L18 2" fill="none" stroke="#999" stroke-width="2"/>
  </svg>
  <div class="why-item">30 Day Money Back<br>Guarantee</div>
</aside>

</body>
</html>
```